Picture Ads

We need some banner ads for our home business opportunity, we are evolving from text to picture ads. I have added some examples of what other distributors are using. We are looking for something really eye catching with some good key words and nice bright colours and to include our photo (attached)
Key words to include:
Booming online business
Personal Development and Leadership Industry
Earn an executive income from home
Simple 3 step system
Make up to $5,000 per sale
Not MLM
The size needs to be: 1000 x 35 pixels
13.9 x 4.75 Inches
35.3 x 11.1 cm
I think different platforms accept different sizes, not too familiar with it yet, any guidance welcome. I've clicked project for 2 days if that is to prioritise the order?
Many thanks,
Maren

Industry/Entity Type

Business

```html
<!DOCTYPE html>
<html lang="en">
<head>
<meta charset="utf-8">
<title>Booming Online Business Banner</title>
<link href="https://fonts.googleapis.com/css2?family=Black+Ops+One&family=Arimo:wght@400;700&family=Oswald:wght@600&family=Kalam:wght@400&display=swap" rel="stylesheet">
<style>
  :root {
    --sky-deep: #0a5fd8;
    --sky-mid: #1e8cf0;
    --sky-light: #7fd4ff;
    --gold-top: #fff36a;
    --gold-bottom: #f0a800;
    --title-edge: #6b4a00;
    --lime: #e8ff3c;
    --white: #ffffff;
    --tick: #3ddc3d;
    --cross: #e8262b;
    --money: #44ff5a;
    --btn-top: #ffc21a;
    --btn-bottom: #f27a00;
    --frame: #ffffff;
    --ink: #333333;
  }
  * { margin: 0; padding: 0; box-sizing: border-box; }
  html, body { width: 1200px; height: 410px; overflow: hidden; background: #ffffff; }
  .banner {
    position: relative;
    width: 1200px;
    height: 410px;
    overflow: hidden;
    background:
      radial-gradient(ellipse 420px 160px at 780px 120px, rgba(255,255,255,0.55), transparent 70%),
      radial-gradient(ellipse 600px 260px at 900px 330px, rgba(140,225,255,0.5), transparent 70%),
      linear-gradient(160deg, var(--sky-deep) 0%, var(--sky-mid) 45%, var(--sky-light) 75%, var(--sky-mid) 100%);
  }
  .streaks { position: absolute; inset: 0; }
  .headline {
    position: absolute;
    left: 10px; top: 4px;
    font-family: "Black Ops One", sans-serif;
    font-size: 72px;
    letter-spacing: 2px;
    line-height: 1;
    background: linear-gradient(180deg, var(--gold-top) 20%, var(--gold-bottom) 85%);
    -webkit-background-clip: text;
    background-clip: text;
    color: transparent;
    -webkit-text-stroke: 1.5px var(--title-edge);
    filter: drop-shadow(2px 3px 2px rgba(0,0,0,0.35));
    white-space: nowrap;
  }
  .growth-arrow { position: absolute; left: 1078px; top: 22px; }
  .tagline {
    position: absolute;
    left: 26px; top: 98px;
    font-family: "Arimo", sans-serif;
    font-size: 38px;
    color: var(--lime);
    text-shadow: 1px 2px 2px rgba(0,40,120,0.45);
    white-space: nowrap;
  }
  .benefits { position: absolute; left: 24px; top: 154px; list-style: none; }
  .benefits li {
    display: flex; align-items: center;
    height: 40px;
    font-family: "Arimo", sans-serif;
    font-size: 30px;
    color: var(--white);
    text-shadow: 1px 2px 2px rgba(0,40,120,0.4);
    white-space: nowrap;
  }
  .benefits li svg { margin-right: 14px; flex: none; }
  .amount { color: var(--money); }
  .cta {
    position: absolute;
    left: 66px; top: 328px;
    width: 262px; height: 66px;
    border-radius: 8px;
    background: linear-gradient(180deg, var(--btn-top), var(--btn-bottom));
    box-shadow: 0 3px 6px rgba(0,0,0,0.35);
    display: flex; align-items: center;
    text-decoration: none;
  }
  .cta-label {
    flex: 1;
    text-align: center;
    font-family: "Oswald", sans-serif;
    font-size: 34px;
    color: var(--white);
    text-shadow: 1px 2px 2px rgba(120,50,0,0.5);
    letter-spacing: 0.5px;
  }
  .cta-arrow {
    width: 64px; height: 100%;
    border-left: 2px solid rgba(255,255,255,0.45);
    display: flex; align-items: center; justify-content: center;
  }
  .snapshot {
    position: absolute;
    left: 930px; top: 90px;
    width: 252px; height: 306px;
    background: var(--frame);
    padding: 12px 12px 0;
    transform: rotate(2deg);
    box-shadow: 2px 4px 10px rgba(0,0,0,0.45);
  }
  .snapshot-photo {
    width: 228px; height: 254px;
    background: radial-gradient(ellipse at 60% 55%, #c7a07a 0%, #7a5540 45%, #3a2a24 100%);
  }
  .snapshot-caption {
    text-align: center;
    font-family: "Kalam", cursive;
    font-size: 14px;
    color: var(--ink);
    margin-top: 8px;
  }
</style>
</head>
<body>
<div class="banner">
  <svg class="streaks" width="1200" height="410" viewBox="0 0 1200 410" aria-hidden="true">
    <path d="M300 410 C 600 250, 850 180, 1200 140 L1200 170 C 860 210, 620 280, 360 410 Z" fill="rgba(255,255,255,0.18)"/>
    <path d="M500 410 C 750 300, 950 240, 1200 230 L1200 250 C 960 262, 780 320, 560 410 Z" fill="rgba(255,255,255,0.22)"/>
    <path d="M450 0 C 650 90, 850 120, 1200 80 L1200 96 C 840 140, 640 110, 430 0 Z" fill="rgba(255,255,255,0.15)"/>
  </svg>

  <h1 class="headline">BOOMING ONLINE BUSINESS</h1>

  <svg class="growth-arrow" width="92" height="58" viewBox="0 0 92 58" aria-hidden="true">
    <polyline points="4,52 30,28 46,40 76,12" fill="none" stroke="#2bd14a" stroke-width="11" stroke-linejoin="round" stroke-linecap="round"/>
    <polygon points="62,2 90,0 88,28" fill="#2bd14a"/>
  </svg>

  <p class="tagline">Personal Development and Leadership Industry</p>

  <ul class="benefits">
    <li><svg width="24" height="22" viewBox="0 0 24 22" aria-hidden="true"><path d="M2 12 L9 19 L22 3" fill="none" stroke="var(--tick)" stroke-width="5" stroke-linecap="round" stroke-linejoin="round"/></svg>Earn an executive income from home</li>
    <li><svg width="24" height="22" viewBox="0 0 24 22" aria-hidden="true"><path d="M2 12 L9 19 L22 3" fill="none" stroke="var(--tick)" stroke-width="5" stroke-linecap="round" stroke-linejoin="round"/></svg>Simple 3 step system</li>
    <li><svg width="24" height="22" viewBox="0 0 24 22" aria-hidden="true"><path d="M2 12 L9 19 L22 3" fill="none" stroke="var(--tick)" stroke-width="5" stroke-linecap="round" stroke-linejoin="round"/></svg>Make up to&nbsp;<span class="amount">$5,000</span>&nbsp;per sale</li>
    <li><svg width="24" height="22" viewBox="0 0 24 22" aria-hidden="true"><path d="M4 3 L20 19 M20 3 L4 19" fill="none" stroke="var(--cross)" stroke-width="5" stroke-linecap="round"/></svg>Not MLM</li>
  </ul>

  <a class="cta" href="#">
    <span class="cta-label">GET STARTED</span>
    <span class="cta-arrow">
      <svg width="30" height="34" viewBox="0 0 30 34" aria-hidden="true"><path d="M6 3 L24 17 L6 31" fill="none" stroke="#c85a00" stroke-width="7" stroke-linejoin="round" stroke-linecap="round"/></svg>
    </span>
  </a>

  <figure class="snapshot">
    <div class="snapshot-photo" role="img" aria-label="Photo of Maren and Rhoda Ellison smiling together"></div>
    <figcaption class="snapshot-caption">Maren and Rhoda Ellison</figcaption>
  </figure>
</div>
</body>
</html>
```